Greek Souvlaki Restaurant Menu Design

We would like to redesign our menu (at the moment just a price-list without any graphics) and create something more fun.

You can find all the items we are offering at the following link / our e-shop:
https://olivebranchkitchen.example/orders/en/order/
I have also attached a printout of the above with hand written notes on the sections and items that will be included.

Our menu is divided to a couple of parts:
- Souvlaki Bar and Grill
- Authentic Greek Cuisine
- Wine List
- Desserts
- Bakaliko

This project will take on the first part of our menu, which is the Souvlaki Bar and Grill. If we are happy with your design, we will then develop the rest of our menu.

Souvlaki Bar and Grill
---------------------------

Our souvlaki can be customised to the customer requirements. The following links have similar set ups:

WOW!Patty
https://gr.pinboardly.example/pin/100000000000000001/
I like the way they have set it up, but the graphics and colours used are not my thing. I also like they way they have split up the steps, choose, top it of, etc.

The Krokk
https://gr.pinboardly.example/pin/100000000000000002/
I hate the step 1,2,3 on the left side. It does not make it playful. Like the fact that they have used pictures of the ingredients.

https://gr.pinboardly.example/pin/100000000000000003/
Hate the graphics, like the concept.

-------------

First Sections: Our Souvliaki Pita Wrap

The steps to customise a souvlaki can be found on the following link:
https://olivebranchkitchen.example/orders/en/order/ and choose pita wrap.

Most of the one side of our Souvliaki/Grill menu should be dedicated to our Pita Wraps.

It should have a small description of the Greek Souvlaki Pita Wrap. Something along the lines of "Get a whole meal all wrapped up with our delicious Greek Pita Wraps. Containing protein, sauce and salad". Improvements of this line are welcome.

It should then have the steps to customise it.

Step One.
Choose Base:
1. Chicken Skewer
2. Pork Skewer
3. etc
Price and options can be found on the above link on our website

Step Two.
Add one of our delicious home made sauces.
Options can be found on our website.

Step Three
Finalise it with the ingredients of your choice.
The customer can select multiple incredients

Step Four.
Feeling Hungry? Add extras:
Extras and Prices can be found on the link provided.

Buy two wraps and save. Takeaway only!
You will find this option as "Double Souvlaki Pita Wrap Offer."
Instead of 2x5.5 = £11 pay £10.5. This offer should also be mentioned somewhere on this section.

-----

Second Section - Our Platters

Skewers Platter and Gyros Platter

Options can be found by clicking on the items on the link provided.

Extras and Pita Bread option are common. Meat options are different and skewers have a choice of side. Meat options have 2/3 skewers and 200/300 grams of gyros, so they can probably be combined somehow.

These section can also be called Naked / Open Souvlaki Platters

Third Section
From Our Grill

All options from this section together with modifiers (can be see if you click on each item). I would like pictures from each item.

Forth Section
Meal Deals, starter combo and Set Menu.

Meal Deal for 1/2 and 4 are wraps with extras. The for 4 is not on the pdf and will be up on our website soon, so please check. I think those are easy to e incorporated next to the pita wrap section as upgrades to save.

Set menus are various items.

If they can fit on this page somehow we incorporate them, if not we can make a separate page with the offers / meals deals. If a separate page is created them the meal deal from our kitchen and vegetarean set menu should also be included.

Fifth Section
Salads and Starter

I would like all options from Hot and Cold starter and our salad. I would like pictures next to all options, if possible.

-----

Final notes/ideas.

Wraps, platters and grill could be one page front and back. Salads and starters could be a different page(s) or sections.

The menu should be easily updated and we would like a format where we can update prices and descriptions.

Prices and descriptions can be found on the link provided.

Feel free to improve our descriptions and titles. Please do mention where you made improvements, so we can approve them.

Our kitchen, dessert and wine menu will be given as a separate project and priority will be given to the person that won this competition.

If you need better quality pictures please let us know, most of the pictures we do have them in raw format too.

------

Some designs that I like. To give you an idea of the design I would like to see:

https://www.craftmarketly.example/listing/100000001/american-menu-restaurant-cafe-menus
I would love to see something like that for the grill/salad/starter side of our menu, since it has space for pictures.

https://gr.pinboardly.example/pin/100000000000000004/
I would love to see something like that, where the incredients of a souvlaki come together. This is optional and does not have to be there.

https://gr.pinboardly.example/pin/100000000000000005/

https://gr.pinboardly.example/pin/100000000000000006/

https://gr.pinboardly.example/pin/100000000000000007/

https://gr.pinboardly.example/pin/100000000000000008/

Target Market(s)

London

Font styles to use
Serif
Sans Serif

Colors
abd037
3277b5
33a6d7

Requirements
Must have
• Build your own souvlaki section. See description for examples.

Pictures for starters and salads.

Should be elegant
Nice to have
• Incorporate our relevant meal deals on the souvlaki pita section

```html
<!DOCTYPE html>
<html lang="en">
<head>
<meta charset="utf-8">
<title>Souvlaki – Pita Wrap Menu</title>
<link rel="stylesheet" href="https://fonts.googleapis.com/css2?family=Lobster&family=Source+Sans+3:wght@300;400;600&display=swap">
<style>
  :root{
    --backdrop:#e8e8e8;
    --paper:#ffffff;
    --band:#adc6e6;
    --frame:#b3cbe8;
    --rule:#b8cfe9;
    --accent:#5b97d0;
    --ink:#242424;
    --dots:#9fbde0;
  }
  html,body{margin:0;padding:0;width:1200px;height:1200px;overflow:hidden;background:var(--backdrop);}
  .page{position:absolute;left:191px;top:22px;width:929px;height:1313px;background:var(--paper);
    transform:scale(0.88);transform-origin:0 0;font-family:"Source Sans 3",Arial,sans-serif;color:var(--ink);}
  .page *{position:absolute;margin:0;}
  .brand{left:62px;top:70px;width:160px;color:var(--ink);font-weight:400;font-size:24px;line-height:30px;white-space:nowrap;}
  .title-band{left:230px;top:52px;width:664px;height:65px;background:var(--band);}
  .title-band h1{left:0;right:0;top:2px;text-align:center;color:#fff;font-family:"Lobster",cursive;font-weight:400;font-size:46px;}
  .frame{left:33px;top:145px;width:857px;height:1128px;border:3px solid var(--frame);}
  .photo{left:88px;top:168px;width:208px;height:152px;border-radius:9px;
    background:linear-gradient(135deg,#6f9cc9 0%,#c9a06a 45%,#a8793f 60%,#5e8ec2 100%);}
  .intro-title{left:300px;width:568px;text-align:center;color:var(--accent);white-space:nowrap;}
  .intro-title.main{top:150px;font-size:34px;font-weight:400;}
  .intro-title.sub{top:186px;font-size:25.5px;letter-spacing:2px;}
  .intro-text{left:328px;top:222px;width:514px;font-size:16.3px;line-height:20.6px;font-weight:300;text-align:justify;}
  .rule{left:55px;width:819px;height:2px;background:var(--rule);}
  .section-title{left:55px;width:819px;text-align:center;color:var(--accent);font-size:20px;line-height:26px;font-weight:600;white-space:nowrap;}
  .section-title em{font-style:italic;}
  .food{border-radius:40%;}
  .name{font-size:18px;line-height:22px;white-space:nowrap;}
  .price{font-size:18.5px;text-align:right;width:120px;white-space:nowrap;}
  .dots{height:0;border-top:4px dotted var(--dots);}
  .sauce{width:54px;height:54px;border-radius:50%;border:2px solid #333;box-sizing:border-box;}
</style>
</head>
<body>
<main class="page">
  <div class="brand">Agora Grill</div>
  <header class="title-band"><h1>Souvlaki</h1></header>
  <div class="frame"></div>

  <div class="photo" role="img" aria-label="Photo of a souvlaki pita wrap with fries in branded paper"></div>
  <h2 class="intro-title main">PITA WRAP</h2>
  <p class="intro-title sub">- MAKE IT YOUR OWN -</p>
  <p class="intro-text">Get a whole meal all wrapped up with our Greek pita wraps . Choose the base (meat skewers, gyros, halloumi or kebab) you want. Then add one of our delicious home made sauces. Finalise it with the ingredients of your choice. If you are feeling extra hungry you can double up your pita or add extra base. It will leave you craving them time and time again.</p>

  <div class="rule" style="top:350px"></div>
  <h3 class="section-title" style="top:351px">WRAP BASE</h3>
  <div class="rule" style="top:376px"></div>

  <div class="food" style="left:97px;top:390px;width:70px;height:48px;background:radial-gradient(#a0522d,#5a2a14)" role="img" aria-label="Grilled chicken"></div>
  <p class="name" style="left:214px;top:403px">Chicken</p><p class="price" style="left:325px;top:403px">+ £ 0.50</p>
  <div class="food" style="left:112px;top:450px;width:55px;height:52px;background:radial-gradient(#d9a89a,#a2665a)" role="img" aria-label="Pork chop"></div>
  <p class="name" style="left:214px;top:466px">Pork</p><p class="price" style="left:325px;top:466px">+ £ 0.50</p>
  <div class="food" style="left:110px;top:518px;width:72px;height:42px;background:radial-gradient(#b07a45,#6a4522)" role="img" aria-label="Chicken gyros"></div>
  <p class="name" style="left:214px;top:528px">Gyros Chicken</p><p class="price" style="left:329px;top:528px">+ £ 1.50</p>
  <div class="food" style="left:117px;top:578px;width:64px;height:50px;background:radial-gradient(#8a3b1e,#3a1a0e)" role="img" aria-label="Pork gyros"></div>
  <p class="name" style="left:214px;top:590px">Gryos Pork</p><p class="price" style="left:325px;top:590px">+ £ 1.50</p>
  <div class="food" style="left:112px;top:642px;width:72px;height:58px;background:radial-gradient(#8a5a30,#3e2412)" role="img" aria-label="Mixed gyros"></div>
  <p class="name" style="left:214px;top:653px">Mixed Gryos<br>(chicken and pork)</p><p class="price" style="left:325px;top:653px">+ £ 2.00</p>

  <div class="food" style="left:524px;top:400px;width:56px;height:46px;background:radial-gradient(#6b3a22,#2a140a)" role="img" aria-label="Kebab"></div>
  <p class="name" style="left:600px;top:403px">Kebab<br>(lamb + beef)</p><p class="price" style="left:711px;top:403px">+ £ 0.50</p>
  <div class="food" style="left:519px;top:474px;width:63px;height:40px;background:radial-gradient(#c0502a,#6e2410)" role="img" aria-label="Grilled sausages"></div>
  <p class="name" style="left:600px;top:487px">Sausage</p><p class="price" style="left:711px;top:487px">+ £ 0.50</p>
  <div class="food" style="left:520px;top:540px;width:62px;height:52px;background:linear-gradient(135deg,#f3e2b8,#c8894a)" role="img" aria-label="Grilled halloumi"></div>
  <p class="name" style="left:600px;top:550px">Haloumi (V)</p><p class="price" style="left:711px;top:550px">+ £ 0.50</p>
  <div class="dots" style="left:532px;top:626px;width:48px"></div>
  <p class="name" style="left:600px;top:612px">No base (V)</p>

  <div class="rule" style="top:727px"></div>
  <h3 class="section-title" style="top:728px">Wrap Sauce</h3>
  <div class="rule" style="top:753px"></div>
  <div class="sauce" style="left:170px;top:770px;background:radial-gradient(#ffffff,#d7e3d0)" role="img" aria-label="Tzatziki"></div>
  <p class="name" style="left:254px;top:790px">Tzatziki (V)</p>
  <div class="sauce" style="left:170px;top:837px;background:radial-gradient(#f6d8c8,#d39a82)" role="img" aria-label="Burger sauce"></div>
  <p class="name" style="left:254px;top:852px">Burger Sauce</p>
  <div class="sauce" style="left:565px;top:770px;background:radial-gradient(#e8b772,#c88a45)" role="img" aria-label="Tyrokafteri"></div>
  <p class="name" style="left:648px;top:790px">Tyrokafteri (V)</p>
  <div class="dots" style="left:572px;top:860px;width:48px"></div>
  <p class="name" style="left:648px;top:852px">No Sauce</p>

  <div class="rule" style="top:917px"></div>
  <h3 class="section-title" style="top:918px">Wrap Ingredients ( Choose 1 ) <em>Required</em></h3>
  <div class="rule" style="top:943px"></div>
  <div class="food" style="left:105px;top:966px;width:74px;height:42px;background:linear-gradient(120deg,#ffd44a,#f0a818)" role="img" aria-label="Fries"></div>
  <p class="name" style="left:190px;top:976px">Fries</p>
  <div class="food" style="left:278px;top:964px;width:66px;height:46px;background:radial-gradient(#ff4a2a,#b81a0a)" role="img" aria-label="Tomatoes"></div>
  <p class="name" style="left:352px;top:976px">Tomatoes</p>
  <div class="food" style="left:480px;top:968px;width:60px;height:42px;background:radial-gradient(#d9587a,#7a1236)" role="img" aria-label="Red onions"></div>
  <p class="name" style="left:551px;top:976px">Onions</p>
  <div class="dots" style="left:650px;top:984px;width:48px"></div>
  <p class="name" style="left:711px;top:976px">No Ingredients</p>

  <div class="rule" style="top:1030px"></div>
  <h3 class="section-title" style="top:1031px">Wrap Extras</h3>
  <div class="rule" style="top:1056px"></div>
  <div class="food" style="left:97px;top:1072px;width:78px;height:58px;border-radius:50%;background:radial-gradient(#f1cfa0,#d69a5c)" role="img" aria-label="Pita breads"></div>
  <p class="name" style="left:192px;top:1088px">Double Pita Bread</p><p class="price" style="left:303px;top:1088px">+ £ 1.00</p>
  <div class="food" style="left:95px;top:1145px;width:74px;height:42px;background:linear-gradient(160deg,#7a3a1a,#3a1a0a)" role="img" aria-label="Pork skewer"></div>
  <p class="name" style="left:192px;top:1151px">add Pork Skewer</p><p class="price" style="left:303px;top:1151px">+ £ 2.50</p>
  <div class="food" style="left:90px;top:1200px;width:92px;height:48px;background:linear-gradient(160deg,#d9a56a,#9a6632)" role="img" aria-label="Chicken skewer"></div>
  <p class="name" style="left:192px;top:1213px">add Chicken Skewer</p><p class="price" style="left:303px;top:1213px">+ £ 2.50</p>

  <div class="food" style="left:486px;top:1076px;width:54px;height:48px;background:radial-gradient(#6b3a22,#2a140a)" role="img" aria-label="Kebab"></div>
  <p class="name" style="left:559px;top:1088px">add Kebab (lamb+beef)</p><p class="price" style="left:726px;top:1088px">+ £ 2.50</p>
  <div class="food" style="left:481px;top:1145px;width:62px;height:40px;background:radial-gradient(#c0502a,#6e2410)" role="img" aria-label="Grilled sausages"></div>
  <p class="name" style="left:559px;top:1151px">add Sausage</p><p class="price" style="left:726px;top:1151px">+ £ 2.50</p>
  <div class="food" style="left:481px;top:1202px;width:62px;height:50px;background:linear-gradient(135deg,#f3e2b8,#c8894a)" role="img" aria-label="Grilled halloumi"></div>
  <p class="name" style="left:559px;top:1213px">add Haloumi</p><p class="price" style="left:726px;top:1213px">+ £ 1.90</p>
</main>
</body>
</html>
```